Professional Website Design to match new logo for Medical Legal Company

We have rebranded our company and We want a professional but also dynamic web site design for a group of esteemed doctors that provide expert evaluation of an injured worker in a Workers Compensation case.
​
1. Our target market is both the attorneys who select our doctors and any doctors who would wish to join our group.

2. Notes for the Landing Page:
- We prefer a simpler, sleeker more modern look for the landing page.
- We want a simplified landing page with one image, three buttons highlighted in Content document.
- We want the main image to be black and white but it can be splashed with color.
-We think the landing page might be enhanced by add a dark blue or black as a primary color. Of course please feel free to try any color combination you think might work.
- We want "The Meridale Circle" in large letters and "Stewards of a fair and prompt outcome" in small lettering. We don't want icons on the buttons.
- Do not want more than the one picture at top of landing page.
- We do not want any pictures that include faces. Please eliminate or replace. They will not be chosen.
- For the landing page, instead of a second set of photos please experiment with using medical symbols and legal symbols.
​
3. New Company Name: The Meridale Circle
New logo is uploaded bronze and grey/silver will be colors although we are still tweaking the colors for more metallic feel. Want simple not busy.

4. The overall Web page design needs to have some website design effect (e,g image rollover, scrolling effect, hover effect etc).

5. Please follow the attached word document file for the page content of the 4 web pages. Do not mix it up.

Previous company website: www.clinicjuristpanel.example (we wish to convert some of the content from this website to the new brand). Competitor website that we like: www.docboardly.example

Target Market(s)

Professional Elite. Attorneys and Doctors

Industry/Entity Type

Medical Legal

Coding

Coded - Design and coding required

Number of Pages Required

5+ page

Font styles to use
Other font styles liked:
• Helvetica or maybe font that matches logo. We are open

Colors

Designer to choose colors to be used in the design.

Requirements
Must have
• I can't locate on color scale but we want Bronze and Silver/Grey from logo. Additional colors can be added. Various shades of grey
Nice to have
• Black and white photos, simple elegant design
Should not have
• Images with faces of unknown people

```html
<!DOCTYPE html>
<html lang="en">
<head>
<meta charset="utf-8">
<title>The Meridale Circle</title>
<link href="https://fonts.googleapis.com/css2?family=Inter:wght@400;500;600;700&display=swap" rel="stylesheet">
<style>
:root{
  --bronze:#9b5c3d;
  --bronze-dark:#5e3322;
  --heading:#633724;
  --text:#7b7b7b;
  --grey-1:#a9a9ad;
  --grey-2:#c6c6c8;
  --grey-3:#d9d9db;
  --about-bg:#d5d5d6;
  --panel:#e3e3e4;
  --footer:#dcc7bd;
  --symbol:#8a8a8e;
  --white:#ffffff;
}
*{box-sizing:border-box;margin:0;padding:0}
html,body{width:1200px;height:3505px;overflow:hidden}
body{font-family:"Inter",Helvetica,Arial,sans-serif;background:var(--white);color:var(--text);position:relative}
.abs{position:absolute}
.btn{position:absolute;display:flex;align-items:center;justify-content:center;border-radius:6px;font-size:15px;font-weight:500;background:var(--bronze);color:#fff}
.btn.outline{background:transparent;border:1.5px solid var(--bronze);color:var(--bronze)}
.brand{display:flex;align-items:center;gap:10px}
.brand-mark{width:26px;height:26px;background:var(--bronze)}
.brand-name{font-size:22px;font-weight:600;color:var(--bronze-dark);letter-spacing:.5px}
h2.section-title{position:absolute;font-size:34px;font-weight:700;color:var(--heading)}

/* symbol panels: flat tone with a small medical or legal sign */
.symbol-panel{position:absolute;display:flex;align-items:center;justify-content:center}
.symbol-panel svg{opacity:.55}

/* hero */
.hero{position:absolute;left:0;top:0;width:1200px;height:508px;background:linear-gradient(100deg,#3d3d3d 0%,#7c7c7c 35%,#b0b0b0 55%,#5a5a5a 80%,#2c2c2c 100%)}
.site-header{position:absolute;left:0;top:0;width:1200px;height:102px;background:rgba(190,170,160,.45)}
.site-header .brand{position:absolute;left:83px;top:31px}
.main-nav{position:absolute;left:383px;top:41px;display:flex;gap:33px;font-size:15px;color:#5a3424}
.login{left:995px;top:33px;width:121px;height:35px}
.hero-title{position:absolute;left:83px;top:162px;font-size:35px;font-weight:600;color:#fff;letter-spacing:.5px}
.hero-sub{position:absolute;left:83px;top:222px;font-size:19px;color:#fff}
.hero-cta{left:83px;top:267px;width:229px;height:35px}
.slide-arrow{position:absolute;top:222px;width:24px;height:24px;border-radius:50%;background:rgba(255,255,255,.6)}
.dots{position:absolute;left:574px;top:484px;display:flex;gap:7px}
.dots span{width:7px;height:7px;border-radius:50%;background:rgba(255,255,255,.5)}
.dots span.on{background:var(--bronze)}

/* about */
.about{position:absolute;left:0;top:508px;width:1200px;height:413px;background:var(--about-bg)}
.about h2{left:302px;top:60px}
.about-text{position:absolute;left:302px;top:118px;width:505px;font-size:15.5px;line-height:19px}
.about .btn{left:302px;top:221px;width:100px;height:37px}

/* stats */
.stats{position:absolute;left:0;top:921px;width:1200px;height:162px}
.stat{position:absolute;top:36px;width:300px;text-align:center;margin-left:-150px}
.stat b{display:block;font-size:32px;font-weight:600;color:var(--heading)}
.stat span{display:block;margin-top:16px;font-size:20px;color:#7a7a7a}

/* features */
.feature{position:absolute;top:1143px;width:340px}
.feature .icon{position:absolute;left:0;top:0;width:48px;height:48px;border-radius:50%;background:#f0edeb;display:flex;align-items:center;justify-content:center}
.feature h3{position:absolute;left:68px;top:0;width:250px;font-size:20px;line-height:23.5px;font-weight:600;color:var(--heading)}
.feature p{position:absolute;left:68px;width:265px;font-size:14.5px;line-height:17.5px}

.standards-title{left:0;width:1200px;text-align:center;top:1380px}
.tiles{position:absolute;left:0;top:1480px;width:1200px;height:199px;display:flex}
.tile{flex:1;display:flex;flex-direction:column;align-items:center;justify-content:center;gap:12px;text-align:center;font-size:17px;font-weight:600;color:#4a2a1d;line-height:20px;padding:0 65px}
.tile svg{opacity:.6}
.show-more{left:548px;top:1739px;width:102px;height:38px;border-radius:8px}

/* testimonials */
.testimonials{position:absolute;left:0;top:1838px;width:1200px;height:332px}
.testimonials h2{left:653px;top:32px}
.avatar{position:absolute;left:663px;top:124px;width:84px;height:84px;border-radius:50%;background:#b99482;display:flex;align-items:center;justify-content:center}
.bubble{position:absolute;left:810px;top:116px;width:150px;height:110px;border-radius:14px;background:#d6d6d7}
.quote{position:absolute;left:767px;top:122px;width:290px;font-size:14.5px;line-height:17.5px;color:#8a8a8a}
.quote-name{position:absolute;left:884px;top:231px;font-size:16px;font-weight:600;color:var(--heading)}
.quote-role{position:absolute;left:1032px;top:260px;font-size:15px;color:#555}
.chev{position:absolute}

/* news */
.news h2{left:83px;top:2230px}
.show-all{position:absolute;left:1056px;top:2240px;font-size:15px;color:var(--bronze)}
.card{position:absolute;top:2331px;width:333px;height:438px;background:#fff;border-radius:10px;box-shadow:0 2px 10px rgba(0,0,0,.08)}
.card .symbol-panel{left:6px;top:6px;width:321px;height:166px;border-radius:6px}
.card time{position:absolute;left:17px;top:207px;font-size:10px;color:#777}
.card h3{position:absolute;left:17px;top:229px;width:300px;font-size:20px;line-height:23.5px;font-weight:700;color:var(--heading)}
.card p{position:absolute;left:17px;width:300px;font-size:14.5px;line-height:17.5px}
.card .read{position:absolute;left:17px;font-size:15px;font-weight:600;color:var(--heading);display:flex;align-items:center;gap:18px}

/* contact */
.contact{position:absolute;left:0;top:2831px;width:1200px;height:332px;background:linear-gradient(90deg,#f3f2f1 0%,#eeebe9 45%,#e2dcd8 70%,#ecebea 100%)}
.contact h2{left:83px;top:60px}
.contact p{position:absolute;left:83px;top:126px;width:500px;font-size:15.5px;line-height:18px;color:#555}
.contact .btn{top:208px;height:38px}

/* footer */
.site-footer{position:absolute;left:0;top:3163px;width:1200px;height:342px;background:var(--footer)}
.site-footer .brand{position:absolute;left:83px;top:42px}
.footer-about{position:absolute;left:83px;top:116px;width:290px;font-size:13.5px;line-height:15px;color:#4a4a4a}
.legal{position:absolute;left:83px;top:236px;display:flex;gap:26px;font-size:13.5px;color:#333}
.footer-col h4{position:absolute;font-size:15px;font-weight:600;color:#4a3024}
.footer-links{position:absolute;left:563px;top:70px;list-style:none;font-size:13.5px;color:#333}
.footer-links li{height:25.3px}
.reach{position:absolute;left:899px;list-style:none;font-size:13.5px;color:#333}
.reach li{position:absolute;left:0;display:flex;gap:10px;align-items:flex-start;white-space:nowrap;line-height:17px}
.reach .ic{width:20px;height:20px;flex:none}
.divider{position:absolute;left:83px;top:290px;width:1033px;height:1px;background:#a78c80}
.copyright{position:absolute;left:0;width:1200px;top:314px;text-align:center;font-size:13.5px;color:#333;display:flex;justify-content:center;gap:8px;align-items:center}
</style>
</head>
<body>

<section class="hero" role="img" aria-label="Black and white photo of a physician consulting with a client at a desk">
  <header class="site-header">
    <div class="brand"><span class="brand-mark"></span><span class="brand-name">MERIDALE CIRCLE</span></div>
    <nav class="main-nav"><span>Home</span><span>About</span><span>Educations</span><span>Physicians</span><span>News</span><span>Carriers</span></nav>
    <a class="btn login">Member Login</a>
  </header>
  <h1 class="hero-title">Stewards of a Fair and Prompt Outcome</h1>
  <p class="hero-sub">The high standard of medical reporting you expect</p>
  <a class="btn hero-cta">Schedule a QME Appointment</a>
  <svg class="slide-arrow" style="left:32px" viewBox="0 0 24 24"><path d="M14 7l-5 5 5 5" fill="none" stroke="#666" stroke-width="2"/></svg>
  <svg class="slide-arrow" style="left:1144px" viewBox="0 0 24 24"><path d="M10 7l5 5-5 5" fill="none" stroke="#666" stroke-width="2"/></svg>
  <div class="dots"><span></span><span class="on"></span><span></span><span></span></div>
</section>

<section class="about">
  <div class="symbol-panel" style="left:83px;top:84px;width:175px;height:262px;background:linear-gradient(160deg,#e6e6e6,#bdbdbd)">
    <svg width="64" height="64" viewBox="0 0 24 24"><path d="M9 3h6v6h6v6h-6v6H9v-6H3V9h6z" fill="var(--symbol)"/></svg>
  </div>
  <h2 class="section-title">About Us</h2>
  <p class="about-text">The Meridale Circle is a leader in Qualified Medical Evaluations and SIBTF cases in the State of California. Our doctors are dedicated facilitating settlements through rapid, objective and well researched Expert Medical Opinions</p>
  <a class="btn">Learn More</a>
  <div class="symbol-panel" style="left:853px;top:73px;width:263px;height:272px;border-radius:4px;background:linear-gradient(180deg,#d4d4d4,#a9a9a9)">
    <svg width="80" height="80" viewBox="0 0 24 24" fill="none" stroke="#5e5e62" stroke-width="1.3"><path d="M12 3v17M7 20h10M4 6h16M12 3.5v2.5"/><path d="M6 6l-3 7h6zM18 6l-3 7h6z"/><path d="M3 13a3 2 0 006 0M15 13a3 2 0 006 0"/></svg>
  </div>
</section>

<section class="stats">
  <svg class="abs" style="left:0;top:0" width="1200" height="162" viewBox="0 0 1200 162">
    <rect width="1200" height="162" fill="var(--grey-3)"/>
    <polygon points="0,0 450,0 288,162 0,162" fill="var(--grey-1)"/>
    <polygon points="450,0 905,0 746,162 288,162" fill="var(--grey-2)"/>
    <line x1="450" y1="0" x2="292" y2="162" stroke="#fff" stroke-width="5"/>
    <line x1="905" y1="0" x2="750" y2="162" stroke="#fff" stroke-width="5"/>
  </svg>
  <div class="stat" style="left:156px"><b>25+</b><span style="color:#fff">Years Experience</span></div>
  <div class="stat" style="left:601px"><b>500+</b><span>Evaluations Sites</span></div>
  <div class="stat" style="left:1026px"><b>1M+</b><span>Reporting Evaluations</span></div>
</section>

<div class="feature" style="left:85px">
  <div class="icon" style="background:none;border:2px solid var(--bronze)"><svg width="26" height="26" viewBox="0 0 24 24"><path d="M12 3l2.7 5.6 6.1.8-4.5 4.2 1.1 6-5.4-2.9-5.4 2.9 1.1-6L3.2 9.4l6.1-.8z" fill="none" stroke="var(--bronze)" stroke-width="1.6"/></svg></div>
  <h3>Elite amenities for the entire Meridale Circle Community</h3>
  <p style="top:89px">We cater to medical professionals, delivery services, and lawyers with a bespoke experience tailored to each member's individual prerequisites.</p>
</div>
<div class="feature" style="left:434px">
  <div class="icon"><svg width="28" height="28" viewBox="0 0 24 24" fill="none" stroke="var(--bronze)" stroke-width="1.3"><path d="M3 8h8M3 12h12M3 16h8M13 8h8M17 16h4"/><circle cx="12" cy="8" r="1.6"/><circle cx="16" cy="12" r="1.6"/><circle cx="12" cy="16" r="1.6"/></svg></div>
  <h3>Industry's most cutting-edge technology.</h3>
  <p style="top:66px">We allocate resources towards the newest tech to deliver functionality, advantages, and efficiency previously unseen in our field.</p>
</div>
<div class="feature" style="left:784px">
  <div class="icon"><svg width="28" height="28" viewBox="0 0 24 24" fill="none" stroke="var(--bronze)" stroke-width="1.3"><path d="M2 10l4-3 4 2 3-2 4 1 5 3M5 13l4 3 3-1 3 2 4-3M9 11l3 2"/></svg></div>
  <h3>Comprehensive aid, encompassing every community.</h3>
  <p style="top:89px">We offer authoritative health advice to all individuals, regardless of their location in the US, maintaining the comfort of a local physician-patient rapport.</p>
</div>

<h2 class="section-title standards-title">Highest Standard in Medical Reporting</h2>
<div class="tiles">
  <div class="tile" style="background:linear-gradient(160deg,#f4f4f4,#dcdcdc)">
    <svg width="34" height="34" viewBox="0 0 24 24" fill="none" stroke="#5e3322" stroke-width="1.5"><circle cx="12" cy="12" r="9"/><path d="M12 7v5l3 2"/></svg>
    <span>Time Efficient</span></div>
  <div class="tile" style="background:linear-gradient(160deg,#ececec,#cfcfcf)">
    <svg width="34" height="34" viewBox="0 0 24 24" fill="none" stroke="#5e3322" stroke-width="1.5"><rect x="5" y="3" width="14" height="18" rx="1"/><path d="M8 8h8M8 12h8M8 16h5"/></svg>
    <span>Unambiguous, Brief and Understandable</span></div>
  <div class="tile" style="background:linear-gradient(160deg,#f1efee,#dad6d3)">
    <svg width="34" height="34" viewBox="0 0 24 24" fill="#5e3322"><path d="M9 3h6v6h6v6h-6v6H9v-6H3V9h6z"/></svg>
    <span>Detailed and Comprehensive Medical History</span></div>
  <div class="tile" style="background:linear-gradient(160deg,#e6e6e6,#c9c9c9)">
    <svg width="34" height="34" viewBox="0 0 24 24" fill="none" stroke="#5e3322" stroke-width="1.5"><path d="M12 3v17M7 20h10M4 6h16"/><path d="M6 6l-3 7h6zM18 6l-3 7h6z"/></svg>
    <span>Comprehensive Analysis of all aspects</span></div>
</div>
<a class="btn outline show-more">Show More</a>

<section class="testimonials">
  <div class="symbol-panel" style="left:0;top:0;width:600px;height:332px;background:linear-gradient(100deg,#d8d8d8,#a5a5a5 55%,#737373)">
    <svg width="96" height="96" viewBox="0 0 24 24" fill="none" stroke="#4a4a4e" stroke-width="1.2"><path d="M12 3v17M7 20h10M4 6h16"/><path d="M6 6l-3 7h6zM18 6l-3 7h6z"/><path d="M3 13a3 2 0 006 0M15 13a3 2 0 006 0"/></svg>
  </div>
  <div class="abs" style="left:600px;top:0;width:600px;height:332px;background:var(--panel)"></div>
  <h2 class="section-title">What Physicians Are Saying</h2>
  <div class="avatar"><svg width="34" height="34" viewBox="0 0 24 24" fill="#fff" opacity=".8"><path d="M9 3h6v6h6v6h-6v6H9v-6H3V9h6z"/></svg></div>
  <div class="bubble"></div>
  <svg class="abs" style="left:844px;top:224px" width="32" height="26" viewBox="0 0 32 26"><path d="M0 0h32L6 26z" fill="#d6d6d7"/></svg>
  <p class="quote">Meridale Circle is a remarkable, broad-ranging firm. They're attentive to everything from inception to conclusion, guiding me through the intricacies of the medical-legal field as a doctor.</p>
  <p class="quote-name">Dr Lena Marsh M.D.</p>
  <p class="quote-role">QME</p>
  <svg class="chev" style="left:630px;top:191px" width="16" height="16" viewBox="0 0 16 16"><path d="M10 3L5 8l5 5" fill="none" stroke="#333" stroke-width="2"/></svg>
  <svg class="chev" style="left:1087px;top:191px" width="16" height="16" viewBox="0 0 16 16"><path d="M6 3l5 5-5 5" fill="none" stroke="#333" stroke-width="2"/></svg>
</section>

<section class="news">
  <h2 class="section-title">News</h2>
  <a class="show-all">Show All</a>
  <article class="card" style="left:83px">
    <div class="symbol-panel" style="background:linear-gradient(160deg,#d3d6d9,#a3a7ab)"><svg width="48" height="48" viewBox="0 0 24 24" fill="#5a5a5e"><path d="M9 3h6v6h6v6h-6v6H9v-6H3V9h6z"/></svg></div>
    <time>01 March 2023</time>
    <h3>WMLS is now a part of the Meridale Circle community.</h3>
    <p style="top:321px">WMLS, the foremost qualified medical evaluator (QME) firm in Fresno, California, has become a part of the...</p>
    <span class="read" style="top:409px">Read More <svg width="10" height="14" viewBox="0 0 10 14"><path d="M2 2l5 5-5 5" fill="none" stroke="#333" stroke-width="2"/></svg></span>
  </article>
  <article class="card" style="left:433px">
    <div class="symbol-panel" style="background:linear-gradient(160deg,#dbd8d5,#aba59f)"><svg width="52" height="52" viewBox="0 0 24 24" fill="none" stroke="#5a5a5e" stroke-width="1.4"><path d="M12 3v17M7 20h10M4 6h16"/><path d="M6 6l-3 7h6zM18 6l-3 7h6z"/></svg></div>
    <time>01 March 2023</time>
    <h3>Meridale Circle hires Dana Whitlock as Chairman and CEO</h3>
    <p style="top:321px">Harrowgate Capital Partners has declared Dana Whitlock as Chairman and CEO at ...</p>
    <span class="read" style="top:409px">Read More <svg width="10" height="14" viewBox="0 0 10 14"><path d="M2 2l5 5-5 5" fill="none" stroke="#333" stroke-width="2"/></svg></span>
  </article>
  <article class="card" style="left:784px;height:432px">
    <div class="symbol-panel" style="background:linear-gradient(160deg,#d6dbdf,#a2a7ac)"><svg width="50" height="50" viewBox="0 0 24 24" fill="none" stroke="#5a5a5e" stroke-width="1.4"><rect x="5" y="3" width="14" height="18" rx="1"/><path d="M8 8h8M8 12h8M8 16h5"/></svg></div>
    <time>01 March 2023</time>
    <h3>PRE joins the Meridale Circle Community</h3>
    <p style="top:298px">Pacific Review Evaluators, a prominent Los Angeles-based firm offering independent and qualified medical evaluations ...</p>
    <span class="read" style="top:403px">Read More <svg width="10" height="14" viewBox="0 0 10 14"><path d="M2 2l5 5-5 5" fill="none" stroke="#333" stroke-width="2"/></svg></span>
  </article>
</section>

<section class="contact">
  <h2 class="section-title">Contact Us</h2>
  <p>Our broad network of carriers and lawyers, in conjunction with a panel of the country's highly respected medical professionals, forms a community that delivers expert health advice to those requiring assistance.</p>
  <a class="btn" style="left:83px;width:99px">Contact Us</a>
  <a class="btn outline" style="left:200px;width:102px">Learn More</a>
</section>

<footer class="site-footer">
  <div class="brand"><span class="brand-mark"></span><span class="brand-name">MERIDALE CIRCLE</span></div>
  <p class="footer-about">Meridale Circle reigns as a leading provider of authoritative medical viewpoints across America. Our core strength lies in the impartial, professional medical assessments we provide (IME and QME). Yet, we consistently deliver creative, novel services and verticals to our stakeholders.</p>
  <div class="legal"><span>Privacy Policy</span><span>Disclaimer</span></div>
  <div class="footer-col"><h4 style="left:563px;top:35px">Discover</h4></div>
  <ul class="footer-links"><li>Home</li><li>About</li><li>Education</li><li>Physicians</li><li>News</li><li>Carriers</li></ul>
  <div class="footer-col"><h4 style="left:899px;top:35px">Reach Us</h4></div>
  <ul class="reach" style="top:0">
    <li style="top:76px"><svg class="ic" viewBox="0 0 20 20"><rect width="20" height="20" rx="4" fill="#6b3a27"/><path d="M6 4l2 3-1.5 1.5a8 8 0 004 4L12 11l3 2-1 2.5C9 15 5 11 4.5 6z" fill="#fff"/></svg>(800) 555-0142</li>
    <li style="top:110px"><svg class="ic" viewBox="0 0 20 20"><rect width="20" height="20" rx="4" fill="#6b3a27"/><circle cx="10" cy="10" r="6" fill="none" stroke="#fff" stroke-width="1.3"/><path d="M4 10h12M10 4c-3 3-3 9 0 12M10 4c3 3 3 9 0 12" fill="none" stroke="#fff" stroke-width="1.1"/></svg>meridalecircle.example</li>
    <li style="top:143px"><svg class="ic" viewBox="0 0 20 20"><rect width="20" height="20" rx="4" fill="#6b3a27"/><rect x="4" y="6" width="12" height="8" fill="none" stroke="#fff" stroke-width="1.3"/><path d="M4 6l6 5 6-5" fill="none" stroke="#fff" stroke-width="1.3"/></svg>hello@meridalecircle.example</li>
    <li style="top:171px"><svg class="ic" viewBox="0 0 20 20"><path d="M10 1a6 6 0 016 6c0 5-6 12-6 12S4 12 4 7a6 6 0 016-6z" fill="#6b3a27"/><circle cx="10" cy="7" r="2.2" fill="var(--footer)"/></svg><span>2210 Larkspur Ave.<br>&nbsp;4th Floor Fairmont, CA 90000</span></li>
  </ul>
  <div class="divider"></div>
  <p class="copyright"><svg width="18" height="18" viewBox="0 0 18 18"><circle cx="9" cy="9" r="8" fill="none" stroke="#333" stroke-width="1.3"/><path d="M11.5 6.5a3.5 3.5 0 100 5" fill="none" stroke="#333" stroke-width="1.3"/></svg>2024 Meridale Circle. All Rights Reserved.</p>
</footer>

</body>
</html>
```